Strata Edge Supply Business Card Design Challenge

Please create me a simple card using my logo. I'm not looking for anything abstract.
A couple of colours for text and maybe something on the card so the whole card isn't just a white board.
Please send me samples and I'll reply with suggestions to refine the design. Thank you

Reason: The Ormeau address was incorrect in the brief, so I have updated that so the 4 and 5 star submissions can be updated and resubmitted please!!! Sorry and thank you

Target Market(s)

Mining companies and rock producing aggregate companies. Quarries

Industry/Entity Type

Mining

Contact Information for Business Card

Name - Lewis Trenholm / Company Logo AND Strata Edge Supply Pty Ltd / position - Managing Director / address1 - Unit 3, 14 Kestrel Parade, Ormeau 4208 Queensland AU / address2 - PO Box 917, Kelsington 4398 Northvale AU / mobile - 0427 195 864 / phone - 07 5571 9346 / fax - 07 5571 9420 / email - lt@strataedgesupply.example.com.au / website - www.strataedgesupply.example.com.au

Requirements
Must have
• Business details as per the above. The phone and fax numbers will be confirmed before the end of the project. Thank you
• SINGLE SIDED ONLY please on Card, not transparent plastic

```html
<!DOCTYPE html>
<html lang="en">
<head>
<meta charset="utf-8">
<title>Strata Edge Supply – Business Card</title>
<link rel="stylesheet" href="https://fonts.googleapis.com/css2?family=Questrial&display=swap">
<style>
  :root {
    --backdrop: #1c1c1c;
    --card-white: #ffffff;
    --brand-blue: #00a0df;
    --slate: #58595b;
    --rule-light: #e4e4e4;
    --text-light: #ffffff;
    --text-dark: #4d4d4f;
  }
  * { margin: 0; padding: 0; box-sizing: border-box; }
  html, body {
    width: 1200px; height: 902px; overflow: hidden;
    background: var(--backdrop);
    font-family: "Questrial", "Helvetica Neue", Arial, sans-serif;
  }
  .card {
    position: absolute; left: 99px; top: 165px;
    width: 902px; height: 515px;
    border-radius: 22px; overflow: hidden;
    background: var(--card-white);
  }
  .card__top { position: absolute; left: 0; right: 0; top: 0; height: 250px; }
  .brand {
    position: absolute; left: 52px; top: 112px;
    display: flex; align-items: center; gap: 14px;
    white-space: nowrap;
  }
  .brand__mark { width: 26px; height: 26px; background: var(--brand-blue); flex: none; }
  .brand__name { font-size: 32px; line-height: 1; color: var(--slate); }
  .person { position: absolute; right: 52px; top: 80px; text-align: right; white-space: nowrap; }
  .person__name { font-size: 33px; line-height: 1; color: var(--brand-blue); }
  .person__role { font-size: 21px; line-height: 1; color: var(--text-dark); margin-top: 8px; }
  .person__email {
    display: flex; align-items: center; justify-content: flex-end; gap: 9px;
    font-size: 19px; line-height: 1; color: var(--text-dark); margin-top: 22px;
  }
  .person__email svg { width: 21px; height: 19px; flex: none; }
  .card__rule { position: absolute; left: 0; right: 0; top: 250px; height: 4px; background: var(--rule-light); }
  .card__band { position: absolute; left: 0; right: 0; top: 254px; height: 31px; background: var(--brand-blue); }
  .card__base {
    position: absolute; left: 0; right: 0; top: 285px; bottom: 0;
    background: var(--slate); color: var(--text-light);
  }
  .company { position: absolute; left: 47px; top: 16px; font-size: 32px; line-height: 1.1; white-space: nowrap; }
  .contacts { position: absolute; left: 53px; top: 86px; list-style: none; }
  .contacts li, .addresses li {
    display: flex; align-items: flex-start; gap: 12px;
    font-size: 19px; line-height: 27px; white-space: nowrap;
  }
  .icon { width: 22px; height: 27px; flex: none; }
  .icon svg { width: 21px; height: 21px; margin-top: 3px; display: block; }
  .divider {
    position: absolute; left: 462px; top: 89px; width: 2px; height: 102px;
    background: var(--text-light);
  }
  .addresses { position: absolute; left: 482px; top: 86px; list-style: none; }
  .addresses li { margin-bottom: 5px; line-height: 25px; }
</style>
</head>
<body>
  <main class="card">
    <section class="card__top">
      <div class="brand">
        <span class="brand__mark"></span>
        <span class="brand__name">Strata Edge Supply</span>
      </div>
      <div class="person">
        <div class="person__name">Lewis Trenholm</div>
        <div class="person__role">Managing Director</div>
        <div class="person__email">
          <span>lt@strataedgesupply.example.com.au</span>
          <svg viewBox="0 0 24 22" aria-hidden="true"><path d="M2 9 L12 2 L22 9 V20 H2 Z" fill="#00a0df"/><path d="M2 9 L12 15 L22 9" fill="none" stroke="#fff" stroke-width="1.6"/></svg>
        </div>
      </div>
    </section>
    <div class="card__rule"></div>
    <div class="card__band"></div>
    <section class="card__base">
      <div class="company">Strata Edge Supply Pty Ltd</div>
      <ul class="contacts">
        <li><span class="icon"><svg viewBox="0 0 24 24"><rect x="7" y="2" width="10" height="20" rx="2" fill="#00a0df"/><rect x="9" y="5" width="6" height="11" fill="#58595b"/></svg></span>0427 195 864</li>
        <li><span class="icon"><svg viewBox="0 0 24 24"><path d="M6 2 L9 7 L7 9.5 C8.5 12.5 11.5 15.5 14.5 17 L17 15 L22 18 L19.5 22 C11 21 3 13 2 4.5 Z" fill="#00a0df"/></svg></span>07 5571 9346</li>
        <li><span class="icon"><svg viewBox="0 0 24 24"><rect x="7" y="2" width="10" height="6" fill="#00a0df"/><rect x="2" y="9" width="20" height="9" rx="1.5" fill="#00a0df"/><rect x="7" y="15" width="10" height="7" fill="#00a0df" stroke="#58595b" stroke-width="1.2"/></svg></span>07 5571 9420</li>
        <li><span class="icon"><svg viewBox="0 0 24 24"><circle cx="12" cy="12" r="10" fill="#00a0df"/><path d="M6 8 C9 7 10 10 8 12 C7 14 10 16 9 19 M15 4 C14 7 17 8 19 9 M14 14 C16 13 18 15 17 18" fill="none" stroke="#58595b" stroke-width="1.5"/></svg></span>www.strataedgesupply.example.com.au</li>
      </ul>
      <div class="divider"></div>
      <ul class="addresses">
        <li><span class="icon"><svg viewBox="0 0 24 24"><path d="M12 1 C7 1 4 4.5 4 9 C4 14 12 23 12 23 C12 23 20 14 20 9 C20 4.5 17 1 12 1 Z" fill="#00a0df"/><circle cx="12" cy="9" r="3" fill="#58595b"/></svg></span><span>Unit 3, 14 Kestrel Parade,<br>Brenmoor 4391 Northvale AU</span></li>
        <li><span class="icon"><svg viewBox="0 0 24 24"><rect x="2" y="5" width="20" height="14" fill="#00a0df"/><path d="M2 5 L12 13 L22 5 M2 19 L9 11 M22 19 L15 11" fill="none" stroke="#58595b" stroke-width="1.4"/></svg></span><span>PO Box 917, Kelsington 4398<br>Northvale AU</span></li>
      </ul>
    </section>
  </main>
</body>
</html>
```